R7M Meridian Business Card Design

We need a business card created for our New Business "R7M Meridian"<br/><br/>The business card design is up to you however the following information must be on the business card:<br/><br/>Front of the business card -<br/>Email :dorianv@r7mmeridian.nz<br/>Mobile: +64 (0) 22 4871 659<br/>Website: www.r7mmeridian.nz<br/>Card Owner Name: Dorian Valcourt<br/>Company Title: Business Development Manager<br/>Slogan: "The BEST of both worlds". <br/>Logo On the front attached to the design brief<br/><br/>On the back: <br/>Space on the back for 4 more versions of the logo across the bottom of the card indicating different subsidiary brands - R7M Coffee, R7M Arts, R7M ?? (The card will be used for all of these brands - We Will add the extra subsidiary logos to the design once the design is finished (We are a graphics design team). <br/><br/>Other than that we want a premium feeling logo that remains universally usable depending on the business entity that we are using the card for. The use of bright bold colours would be great but we still want the card to feel premium.
Target Market(s)
Gift Design and Manufacturing Companies
Contact Information for Business Card
Front of the business card -
Email :dorianv@r7mmeridian.nz
Mobile: +64 (0) 22 4871 659
Website: www.r7mmeridian.nz
Card Owner Name: Dorian Valcourt
Company Title: Business Development Manager
Slogan: "The BEST of both worlds".
Logo On the front attached to the design brief

```html
<!DOCTYPE html>
<html lang="en">
<head>
<meta charset="utf-8">
<title>R7M Meridian Business Card</title>
<link href="https://fonts.googleapis.com/css2?family=Source+Sans+3:wght@400;600;700&display=swap" rel="stylesheet">
<style>
  :root {
    --page: #d6d6d6;
    --brand-blue: #344a9e;
    --brand-blue-deep: #2a3d8f;
    --ink: #333333;
    --paper: #ffffff;
    --rule: #3a4fa8;
  }
  * { box-sizing: border-box; margin: 0; padding: 0; }
  html, body {
    width: 1200px; height: 900px; overflow: hidden;
    background: var(--page);
    font-family: "Source Sans 3", "Myriad Pro", Arial, sans-serif;
  }
  .canvas { position: relative; width: 1200px; height: 900px; }

  .card {
    position: absolute; width: 540px; height: 310px; overflow: hidden;
    box-shadow: 0 6px 14px rgba(0,0,0,0.22);
  }

  /* Back of card */
  .card-back { left: 50px; top: 130px; background: var(--brand-blue); }
  .back-watermark {
    position: absolute; left: -14px; bottom: -62px;
    font-size: 230px; font-weight: 700; line-height: 1;
    color: var(--brand-blue-deep); letter-spacing: -4px;
  }
  .sub-brands {
    position: absolute; top: 26px; right: 30px;
    display: flex; flex-direction: column; align-items: flex-end; gap: 22px;
  }
  .sub-brand {
    color: var(--paper); font-size: 17px; font-weight: 600; white-space: nowrap; line-height: 1.2;
  }
  .sub-brand:nth-child(odd) { margin-right: 26px; }

  /* Front of card */
  .card-front { left: 610px; top: 460px; background: var(--paper); }
  .brand-name {
    position: absolute; left: 40px; top: 60px;
    font-size: 34px; font-weight: 700; color: var(--brand-blue); line-height: 1;
  }
  .slogan {
    position: absolute; left: 42px; top: 104px;
    font-size: 15px; color: var(--ink);
  }
  .holder {
    position: absolute; right: 34px; top: 136px; text-align: right;
  }
  .holder-name {
    font-size: 17px; font-weight: 700; color: var(--brand-blue); text-transform: uppercase; letter-spacing: 0.3px;
  }
  .holder-title { font-size: 13px; color: var(--ink); margin-top: 1px; }
  .divider {
    position: absolute; left: 40px; right: 24px; top: 184px; height: 1.5px; background: var(--rule);
  }
  .contacts {
    position: absolute; left: 48px; top: 200px; list-style: none;
    font-size: 13.5px; color: var(--ink); line-height: 19px;
  }
  .contacts li { display: flex; align-items: center; gap: 7px; }
  .contacts svg { width: 12px; height: 12px; flex: none; }
</style>
</head>
<body>
<main class="canvas">

  <section class="card card-back" aria-label="Card back">
    <div class="back-watermark" aria-hidden="true">R7M</div>
    <div class="sub-brands">
      <div class="sub-brand">R7M Coffee</div>
      <div class="sub-brand">R7M Arts</div>
      <div class="sub-brand">R7M Coffee</div>
      <div class="sub-brand">R7M Arts</div>
    </div>
  </section>

  <section class="card card-front" aria-label="Card front">
    <div class="brand-name">R7M Meridian</div>
    <p class="slogan">The BEST of both worlds</p>

    <div class="holder">
      <div class="holder-name">Dorian Valcourt</div>
      <div class="holder-title">Business Development Manager</div>
    </div>

    <div class="divider"></div>

    <ul class="contacts">
      <li>
        <svg viewBox="0 0 12 12"><rect x="3" y="0.8" width="6" height="10.4" rx="1" fill="none" stroke="#3a4fa8" stroke-width="1.2"/><circle cx="6" cy="9.3" r="0.6" fill="#3a4fa8"/></svg>
        +64 (0) 22 4871 659
      </li>
      <li>
        <svg viewBox="0 0 12 12"><rect x="0.8" y="2.3" width="10.4" height="7.4" fill="none" stroke="#3a4fa8" stroke-width="1.2"/><path d="M1 2.6 L6 6.6 L11 2.6" fill="none" stroke="#3a4fa8" stroke-width="1.2"/></svg>
        dorianv@r7mmeridian.nz
      </li>
      <li>
        <svg viewBox="0 0 12 12"><circle cx="6" cy="6" r="5" fill="none" stroke="#3a4fa8" stroke-width="1.1"/><ellipse cx="6" cy="6" rx="2.2" ry="5" fill="none" stroke="#3a4fa8" stroke-width="1"/><path d="M1 6 H11 M2 3.5 H10 M2 8.5 H10" stroke="#3a4fa8" stroke-width="0.9"/></svg>
        www.r7mmeridian.nz
      </li>
    </ul>
  </section>

</main>
</body>
</html>
```